Brisk Comet- Energy shot - ....Amazing Energy for Amazing people

To design a creative /unique logo and picture for Brisk Comet Energy/ energy shot product similar to Nine Dawn energy shot...Berry flavor

I want the design to cover the entire bottle. in addition to Logo (Brisk Comet Energy )

So Brisk Comet Energy will be a competitor of Nine Dawn energy and I want a creative,fantastic, attractive design to catch customers eyes, the product will be in similar size 2oz bottle (see attached image). This template is based on a common 2oz bottle size that measures exactly 114mm circumference x 83mm-85mm height (including cap ).
Please include At the top cap a Logo for: Brisk Comet...

Target Market(s)

Young, busy professionals, athletics

Industry/Entity Type

Product

Logo Text

Vopra Energy...Amazing Energy &Taste !

Requirements
Must have
• Creative exciting design...Vopra Energy...Fan
Nice to have
• Be a genius....Be creative...Be Amazing !

```html
<!DOCTYPE html>
<html lang="en">
<head>
<meta charset="utf-8">
<title>Brisk Comet Energy – Energy Shot Label</title>
<link rel="stylesheet" href="https://fonts.googleapis.com/css2?family=Oswald:wght@700&display=swap">
<style>
  :root {
    --page-grey: #e4e4e4;
    --label-black: #0b0b0b;
    --berry-pink: #e6217e;
    --berry-pink-soft: #7a1244;
    --bolt-yellow: #f7e62a;
    --logo-yellow: #f5e23a;
    --ink-black: #111111;
  }
  * { margin: 0; padding: 0; box-sizing: border-box; }
  html, body {
    width: 1200px;
    height: 1168px;
    overflow: hidden;
    background: var(--page-grey);
    font-family: "Oswald", "Arial Narrow", sans-serif;
  }
  .label {
    position: absolute;
    left: 220px;
    top: 40px;
    width: 760px;
    height: 1088px;
    background: var(--label-black);
    overflow: hidden;
  }
  .label-shapes {
    position: absolute;
    inset: 0;
  }
  .cap-logo,
  .main-logo {
    position: absolute;
    left: 0;
    width: 100%;
    text-align: center;
    color: var(--logo-yellow);
    font-weight: 700;
    line-height: 0.95;
    text-transform: none;
  }
  .cap-logo {
    top: 70px;
    font-size: 40px;
  }
  .main-logo {
    top: 430px;
  }
  .main-logo .logo-line-small {
    display: block;
    font-size: 78px;
  }
  .main-logo .logo-line-large {
    display: block;
    font-size: 150px;
  }
  .runner-art {
    position: absolute;
    left: 330px;
    top: 700px;
    width: 100px;
    height: 130px;
    background: var(--bolt-yellow);
    border-radius: 6px;
  }
  .product-type {
    position: absolute;
    left: 0;
    width: 100%;
    top: 960px;
    text-align: center;
    font-size: 48px;
    font-weight: 700;
    letter-spacing: 1px;
    color: var(--ink-black);
  }
  .product-type .accent { color: var(--berry-pink); }
</style>
</head>
<body>
  <main class="label">
    <svg class="label-shapes" width="760" height="1088" viewBox="0 0 760 1088" aria-hidden="true">
      <defs>
        <radialGradient id="berry-glow" cx="0.55" cy="0.55" r="0.6">
          <stop offset="0" stop-color="var(--berry-pink)"/>
          <stop offset="0.65" stop-color="var(--berry-pink)" stop-opacity="0.75"/>
          <stop offset="1" stop-color="var(--berry-pink-soft)" stop-opacity="0"/>
        </radialGradient>
      </defs>
      <polygon class="halftone-zone" role="img" aria-label="Pink halftone dot pattern"
               points="60,420 700,260 760,300 760,880 0,900 0,470"
               fill="url(#berry-glow)"/>
      <polygon class="bolt-band"
               points="0,870 520,830 470,890 760,760 760,1088 0,1088 0,960 120,960 60,1000 300,900 0,920"
               fill="var(--bolt-yellow)"/>
    </svg>

    <div class="cap-logo">Brisk Comet<br>Energy</div>

    <h1 class="main-logo">
      <span class="logo-line-small">Brisk Comet</span>
      <span class="logo-line-large">Energy</span>
    </h1>

    <div class="runner-art" role="img" aria-label="Yellow silhouette of a running athlete with speed lines"></div>

    <p class="product-type">ENERGY <span class="accent">SHOT</span></p>
  </main>
</body>
</html>
```